Flyer design - company flyer

We would like to inform about and advertise our services. There fore we would like to create a flyer with that information. We'll need a design to ge it done. We are looking for a design aligned with our website and logo. CAUTION - new website. current cleverdock.de is old! You can find our new website which should be represented at: beta.cleverdock.de

```html
<!DOCTYPE html>
<html lang="en">
<head>
<meta charset="utf-8">
<title>CleverDock – Company Flyer</title>
<link href="https://fonts.googleapis.com/css2?family=Roboto:wght@400;500;700;900&display=swap" rel="stylesheet">
<style>
:root{
  --brand:#1a6fc0;
  --brand-dark:#0f4f92;
  --ink:#2f3640;
  --muted:#5d6670;
  --paper:#ffffff;
  --stage:#c9ecee;
  --hero-a:#f4f7fa;
  --hero-b:#8fa3b4;
}
*{margin:0;padding:0;box-sizing:border-box}
html,body{width:1200px;height:759px;overflow:hidden}
body{background:var(--stage);font-family:"Roboto",sans-serif;color:var(--ink);position:relative}
.page{position:absolute;top:34px;width:452px;height:640px;background:var(--paper);overflow:hidden;box-shadow:0 6px 22px rgba(0,60,80,.18)}
.page--front{left:74px}
.page--back{left:674px}
.side-label{position:absolute;top:700px;width:452px;text-align:center;font-weight:700;font-size:24px;letter-spacing:.5px;color:#3a3f44}
.side-label--front{left:74px}
.side-label--back{left:674px}

.hero{position:absolute;top:0;right:0;width:300px;height:260px;background:linear-gradient(110deg,var(--hero-a) 0%,#d5dee6 45%,var(--hero-b) 100%)}
.hero-fade{position:absolute;top:0;left:0;width:260px;height:260px;background:linear-gradient(90deg,#fff 0%,rgba(255,255,255,.85) 55%,rgba(255,255,255,0) 100%)}
.curve{position:absolute;left:0;top:0}
.hero-band{position:absolute;left:0;top:0}

.wordmark{position:absolute;top:22px;left:22px;font-weight:900;font-size:19px;letter-spacing:1.5px;color:var(--brand);display:flex;align-items:center;gap:6px;z-index:2}
.wordmark::before{content:"";width:10px;height:10px;background:var(--brand)}

.headline{position:absolute;left:22px;color:var(--brand);font-weight:900;text-transform:uppercase;line-height:1.02;z-index:2}
.page--front .headline{top:64px;font-size:31px}
.headline small{display:block;font-size:20px;margin-top:2px}
.page--back .headline{top:128px;font-size:30px;width:250px}
.subline{position:absolute;left:22px;top:142px;font-size:13px;line-height:1.25;color:var(--ink)}
.subline strong{font-size:16px;font-weight:500;display:block}

.section-title{position:absolute;left:0;width:100%;text-align:center;font-weight:700;font-size:11px;letter-spacing:.4px;color:var(--ink)}
.page--front .section-title{top:268px}
.page--back .section-title{top:440px}

.benefits{position:absolute;top:292px;left:16px;width:420px;display:grid;grid-template-columns:repeat(3,1fr);row-gap:14px;column-gap:10px}
.benefit{text-align:center}
.icon{width:28px;height:28px;border-radius:50%;background:var(--brand);margin:0 auto 5px;display:flex;align-items:center;justify-content:center;box-shadow:0 0 0 3px #dce9f6}
.icon svg{width:15px;height:15px}
.benefit h3,.info h3{font-size:10px;font-weight:500;color:var(--brand);margin-bottom:3px}
.benefit p,.info p{font-size:6.6px;line-height:1.35;color:var(--muted)}

.infos{position:absolute;top:270px;left:14px;width:424px;display:grid;grid-template-columns:repeat(3,1fr);column-gap:10px;align-items:start;z-index:2}
.info{text-align:center}
.info:nth-child(1){margin-top:22px}
.info:nth-child(2){margin-top:8px}

.plans{position:absolute;top:462px;left:16px;width:420px;display:grid;grid-template-columns:repeat(3,1fr);column-gap:10px}
.plan{border:1.5px solid var(--brand);padding:8px 7px;box-shadow:0 3px 8px rgba(0,0,0,.15);background:#fff}
.plan-head{display:flex;gap:6px;align-items:flex-start;margin-bottom:6px}
.plan-head svg{width:14px;height:14px;flex:none}
.plan h4{font-size:7.5px;font-weight:700;text-transform:uppercase;color:var(--ink)}
.price{font-size:6px;color:var(--muted)}
.price b{font-size:12px;color:var(--brand);font-weight:700}
.plan ul{list-style:none}
.plan li{font-size:6.4px;color:var(--muted);line-height:1.45;padding-left:8px;position:relative}
.plan li::before{content:"✓";position:absolute;left:0;color:var(--brand);font-weight:700}

.contact{position:absolute;left:0;bottom:0;width:100%;height:24px;background:var(--brand);display:flex;justify-content:center;align-items:center;gap:18px;color:#fff;font-size:8px}
.contact span{display:flex;align-items:center;gap:4px}
.contact svg{width:9px;height:9px}
</style>
</head>
<body>

<section class="page page--front">
  <div class="hero" role="img" aria-label="Photo of a businessman holding a glowing padlock shield icon above his open hand"></div>
  <div class="hero-fade"></div>
  <svg class="curve" width="452" height="640" viewBox="0 0 452 640">
    <path d="M0,262 L210,262 Q238,262 262,246 L452,190 L452,640 L0,640 Z" fill="#fff"/>
    <path d="M0,256 L208,256 Q236,256 260,240 L452,184" fill="none" stroke="var(--brand)" stroke-width="3"/>
  </svg>
  <div class="wordmark">CLEVERDOCK</div>
  <h1 class="headline">Safe, Fast<small>and Innovative</small></h1>
  <p class="subline">We Offer Central IT Services<strong>From Highly Secure<br>German Data Centers</strong></p>

  <h2 class="section-title">AN OVERVIEW OF YOUR BENEFITS</h2>
  <div class="benefits">
    <div class="benefit"><div class="icon"><svg viewBox="0 0 16 16"><circle cx="8" cy="8" r="6" fill="none" stroke="#fff" stroke-width="1.6"/><path d="M8 4v4l3 2" fill="none" stroke="#fff" stroke-width="1.6"/></svg></div><h3>Express Suppression</h3><p>From Monday to Friday, the troubleshooting is carried out in a maximum of 8 hours by CleverDock Support.</p></div>
    <div class="benefit"><div class="icon"><svg viewBox="0 0 16 16"><path d="M8 2l4 6H9.5v6h-3V8H4z" fill="#fff"/></svg></div><h3>Fast Programs</h3><p>Our technology gets the maximum speed out of your existing applications.</p></div>
    <div class="benefit"><div class="icon"><svg viewBox="0 0 16 16"><path d="M8 1.5l5.5 2v4c0 3.5-2.5 6-5.5 7-3-1-5.5-3.5-5.5-7v-4z" fill="#fff"/><path d="M5.5 8l2 2 3-3.5" fill="none" stroke="var(--brand)" stroke-width="1.5"/></svg></div><h3>Professional Protection</h3><p>Our service includes professional protection against viruses, crypto viruses, Trojans and other pests.</p></div>
    <div class="benefit"><div class="icon"><svg viewBox="0 0 16 16"><rect x="3" y="2.5" width="10" height="11" rx="1" fill="#fff"/><path d="M5 5.5h6M5 8h6M5 10.5h6" stroke="var(--brand)" stroke-width="1.2"/></svg></div><h3>Data Backup</h3><p>Daily data backup and thus protection against data loss – controlled by us and can be restored at any time.</p></div>
    <div class="benefit"><div class="icon"><svg viewBox="0 0 16 16"><circle cx="8" cy="6.5" r="3" fill="#fff"/><path d="M2 12q3-2 6 0t6 0" fill="none" stroke="#fff" stroke-width="1.6"/></svg></div><h3>Sustained</h3><p>The server systems used are operated with regenerative energies from the electricity supplier Rheinwerk Energie.</p></div>
    <div class="benefit"><div class="icon"><svg viewBox="0 0 16 16"><rect x="2.5" y="4" width="11" height="8" rx="1" fill="#fff"/><text x="8" y="10.6" font-size="6.5" font-weight="700" text-anchor="middle" fill="var(--brand)" font-family="Roboto,sans-serif">€</text></svg></div><h3>Predictable Costs</h3><p>Linear monthly cost distribution. There are no additional costs due to defects, extensions or expensive on-site operations.</p></div>
    <div class="benefit"><div class="icon"><svg viewBox="0 0 16 16"><path d="M3 8a5 5 0 0 1 9-3M13 8a5 5 0 0 1-9 3" fill="none" stroke="#fff" stroke-width="1.7"/><path d="M12.5 2v3.2H9.3M3.5 14v-3.2h3.2" fill="none" stroke="#fff" stroke-width="1.5"/></svg></div><h3>Updates</h3><p>Central update of your operating system with functionalities and security updates.</p></div>
    <div class="benefit"><div class="icon"><svg viewBox="0 0 16 16"><rect x="4" y="7" width="8" height="6.5" rx="1" fill="#fff"/><path d="M5.7 7V5a2.3 2.3 0 0 1 4.6 0v2" fill="none" stroke="#fff" stroke-width="1.5"/></svg></div><h3>High Security</h3><p>Central IT services from highly secure data centers.</p></div>
    <div class="benefit"><div class="icon"><svg viewBox="0 0 16 16"><rect x="2" y="3" width="12" height="9" rx="1" fill="#fff"/><path d="M4 5.5h8M4 8h5" stroke="var(--brand)" stroke-width="1.2"/><path d="M6 14h4" stroke="#fff" stroke-width="1.5"/></svg></div><h3>Familiar Software</h3><p>The user interface looks like you are used to.</p></div>
  </div>

  <footer class="contact">
    <span><svg viewBox="0 0 10 10"><path d="M2 1l2 2-1 1.2q1 2 2.8 2.8L7 6l2 2-1.2 1.5Q4.5 9.5.5 2.2z" fill="#fff"/></svg>+49 2924 5550142</span>
    <span><svg viewBox="0 0 10 10"><rect x="1" y="2" width="8" height="6" fill="#fff"/><path d="M1 2l4 3 4-3" fill="none" stroke="var(--brand)" stroke-width=".9"/></svg>kunde@cleverdock.de</span>
    <span><svg viewBox="0 0 10 10"><circle cx="5" cy="5" r="4" fill="none" stroke="#fff" stroke-width="1"/><path d="M1 5h8M5 1q-2.5 4 0 8M5 1q2.5 4 0 8" fill="none" stroke="#fff" stroke-width=".8"/></svg>www.cleverdock.de</span>
  </footer>
</section>

<section class="page page--back">
  <svg class="hero-band" width="452" height="640" viewBox="0 0 452 640">
    <defs>
      <linearGradient id="backHeroTone" x1="0" y1="0" x2="1" y2="0.3">
        <stop offset="0" stop-color="#ffffff"/>
        <stop offset="0.35" stop-color="#eef2f6"/>
        <stop offset="1" stop-color="#9fb3c4"/>
      </linearGradient>
    </defs>
    <path role="img" aria-label="Photo of a smiling man in a light blue shirt working at a laptop in a bright office" d="M0,118 L160,100 Q200,96 222,82 L452,22 L452,195 L0,300 Z" fill="url(#backHeroTone)"/>
    <path d="M0,118 L160,100 Q200,96 222,82 L452,22" fill="none" stroke="var(--brand)" stroke-width="3"/>
  </svg>
  <div class="wordmark">CLEVERDOCK</div>
  <h1 class="headline">IT That Simply Works</h1>

  <div class="infos">
    <div class="info"><div class="icon"><svg viewBox="0 0 16 16"><path d="M8 2l6.5 11.5h-13z" fill="#fff"/><path d="M8 6.5v3.5M8 11.5v.8" stroke="var(--brand)" stroke-width="1.4"/></svg></div><h3>The Problem</h3><p>From Monday to Friday, the troubleshooting in addition to the human factor, the basis of the IT problems that make your day-to-day business unnecessarily difficult is the computer itself, because viruses land there, programs become lame and data is lost. Troubleshooting is carried out in a maximum of 8 hours by CleverDock Support.</p></div>
    <div class="info"><div class="icon"><svg viewBox="0 0 16 16"><path d="M8 2a4 4 0 0 1 2.5 7.1V11h-5V9.1A4 4 0 0 1 8 2z" fill="#fff"/><path d="M6 12.5h4M6.5 14h3" stroke="#fff" stroke-width="1.2"/></svg></div><h3>Our Solution</h3><p>CleverDock offers you a solution that ensures the daily backup of your data and the monitoring of your system. We start with the basics: everything you need to work is transferred to the servers of our data center. We implement all necessary legal and other requirements there.</p></div>
    <div class="info"><div class="icon"><svg viewBox="0 0 16 16"><path d="M8 1.5l5.5 2v4c0 3.5-2.5 6-5.5 7-3-1-5.5-3.5-5.5-7v-4z" fill="#fff"/><path d="M5.5 8l2 2 3-3.5" fill="none" stroke="var(--brand)" stroke-width="1.5"/></svg></div><h3>Professional Protection</h3><p>If you are wondering how secure our solution is, the answer is very simple: very secure. We work with Nordhaven Data, one of the largest data centers in Germany. The security precautions of this data center are similar to those of a high-security wing. Your data there is protected against malware, unauthorized access and even natural disasters, and in the event of a power failure, generators and backup batteries ensure continuous operation.</p></div>
  </div>

  <h2 class="section-title">SELECT SERVICE</h2>
  <div class="plans">
    <div class="plan">
      <div class="plan-head"><svg viewBox="0 0 16 16"><circle cx="8" cy="5" r="3" fill="var(--brand)"/><path d="M2.5 15q0-5.5 5.5-5.5t5.5 5.5z" fill="var(--brand)"/></svg><div><h4>Thin Client</h4><div class="price">from <b>€ 89</b><br>per user / month</div></div></div>
      <ul><li>Minimum term is 12 months</li><li>Thin client per user included</li><li>Licensing of the Vantix operating system</li><li>Max. 8 hours reaction time</li></ul>
    </div>
    <div class="plan">
      <div class="plan-head"><svg viewBox="0 0 16 16"><rect x="1.5" y="3" width="13" height="8" rx="1" fill="none" stroke="var(--brand)" stroke-width="1.5"/><path d="M0.5 13h15" stroke="var(--brand)" stroke-width="1.5"/></svg><div><h4>Mobile Thin Client</h4><div class="price">from <b>€ 99</b><br>per user / month</div></div></div>
      <ul><li>Minimum term is 12 months</li><li>Support and management</li><li>Licensing of the Vantix operating system</li><li>Max. 8 hours reaction time</li></ul>
    </div>
    <div class="plan">
      <div class="plan-head"><svg viewBox="0 0 16 16"><path d="M8 4a3.5 3.5 0 0 1 2 6.4V12H6v-1.6A3.5 3.5 0 0 1 8 4z" fill="var(--brand)"/><path d="M8 0.5v2M2 3l1.4 1.4M14 3l-1.4 1.4" stroke="var(--brand)" stroke-width="1.2"/></svg><div><h4>Bring Your Own</h4><div class="price">from <b>€ 75</b><br>per user / month</div></div></div>
      <ul><li>No minimum term</li><li>Use with your own device</li><li>Licensing of the Vantix operating system</li><li>Max. 8 hours reaction time</li></ul>
    </div>
  </div>

  <footer class="contact">
    <span><svg viewBox="0 0 10 10"><path d="M2 1l2 2-1 1.2q1 2 2.8 2.8L7 6l2 2-1.2 1.5Q4.5 9.5.5 2.2z" fill="#fff"/></svg>+49 2924 5550142</span>
    <span><svg viewBox="0 0 10 10"><rect x="1" y="2" width="8" height="6" fill="#fff"/><path d="M1 2l4 3 4-3" fill="none" stroke="var(--brand)" stroke-width=".9"/></svg>kunde@cleverdock.de</span>
    <span><svg viewBox="0 0 10 10"><circle cx="5" cy="5" r="4" fill="none" stroke="#fff" stroke-width="1"/><path d="M1 5h8M5 1q-2.5 4 0 8M5 1q2.5 4 0 8" fill="none" stroke="#fff" stroke-width=".8"/></svg>www.cleverdock.de</span>
  </footer>
</section>

<div class="side-label side-label--front">FRONT SIDE</div>
<div class="side-label side-label--back">BACK SIDE</div>

</body>
</html>
```